Require stationery design which includes the following items as a minimum.

- Business card design
- Letterhead
- Envelopes

Details for business card:
Logo: Main logo is called "dove interiors square gold" but you may make use of whichever logo works best.
Tagline: Exquisite Furniture & Furnishings
Name: Helen Marchetti
Title: Interior Stylist
Mobile: 0432 871 264
PH: 03 9572 3140
Email: helen@dove-interiors.com.au

```html
<!DOCTYPE html>
<html lang="en">
<head>
<meta charset="utf-8">
<title>Dove Interiors – Stationery Set</title>
<link rel="stylesheet" href="https://fonts.googleapis.com/css2?family=Cinzel:wght@400&family=Great+Vibes&family=Open+Sans:wght@700&family=Cormorant+Garamond:wght@500&display=swap">
<style>
  :root {
    --paper: #ffffff;
    --ink: #1c1c1c;
    --black-card: #0e0e0e;
    --gold: #b9a64a;
    --gold-light: #e4d9a3;
    --gold-dim: #8c7f3e;
    --pattern-grey: #eceeed;
    --pattern-mid: #9a9a9a;
    --shadow: rgba(0,0,0,0.45);
  }
  * { box-sizing: border-box; margin: 0; padding: 0; }
  html, body { width: 1200px; height: 900px; overflow: hidden; background: var(--paper); }
  .canvas { position: relative; width: 1200px; height: 900px; }

  .sheet { position: absolute; background: var(--paper); box-shadow: 0 0 8px var(--shadow); }

  .brand-name { font-family: "Cinzel", serif; font-weight: 400; color: var(--ink); text-align: center; line-height: 1; }
  .brand-name .word { display: block; }
  .brand-box {
    position: absolute; background: var(--paper); border: 1.5px solid var(--ink); border-radius: 5px;
    display: flex; align-items: center; justify-content: center; gap: 8px;
  }
  .brand-dot { border: 1.5px solid var(--ink); border-radius: 50%; flex: none; }

  .tagline { font-family: "Great Vibes", cursive; position: absolute; text-align: center; white-space: nowrap; }

  /* Letterhead */
  .letterhead { left: 237px; top: 67px; width: 472px; height: 611px; }
  .letterhead .pattern { position: absolute; left: 0; top: 0; width: 100%; height: 128px;
    background: linear-gradient(to bottom, var(--pattern-grey), #f7f8f7 80%, var(--paper)); }
  .letterhead .rule { position: absolute; left: 31px; top: 54px; width: 407px; height: 1px; background: var(--ink); }
  .letterhead .meta { position: absolute; top: 43px; font-family: "Open Sans", sans-serif; font-weight: 700; font-size: 8px; color: var(--ink); }
  .letterhead .phone { left: 41px; }
  .letterhead .note { right: 40px; }
  .letterhead .brand-box { left: 149px; top: 24px; width: 161px; height: 56px; }

  /* Envelopes */
  .envelope-back { left: 604px; top: 424px; width: 514px; height: 224px; }
  .envelope-back .brand-box { left: 22px; top: 23px; width: 92px; height: 23px; gap: 4px; border-width: 1px; }
  .envelope-back .pattern { position: absolute; left: 8px; top: 58px; width: 128px; height: 166px;
    background: radial-gradient(ellipse at center, var(--pattern-grey), var(--paper) 72%); }
  .envelope-front { left: 751px; top: 494px; width: 460px; height: 224px; }
  .envelope-front .brand-name { position: absolute; left: 204px; top: 32px; width: 100px; }
  .envelope-front .tagline { left: 154px; top: 72px; width: 200px; font-size: 11px; color: var(--ink); }

  /* Business cards */
  .card-front { left: 168px; top: 606px; width: 245px; height: 142px; background: var(--black-card); }
  .card-front .mark-ring { position: absolute; left: 110px; top: 35px; width: 24px; height: 24px; border: 1.5px solid var(--gold); border-radius: 50%; }
  .card-front .band { position: absolute; left: 0; top: 74px; width: 100%; height: 20px;
    background: linear-gradient(to right, #6f6420, var(--gold) 18%, #d9cc7c 40%, var(--gold) 70%, #3a3412); }
  .card-front .brand-name { position: absolute; left: 0; top: 76px; width: 100%; color: var(--gold-light); }
  .card-front .tagline { left: 0; top: 121px; width: 100%; font-size: 10px; color: var(--gold-dim); }

  .card-back { left: 387px; top: 675px; width: 251px; height: 145px; display: flex; }
  .card-back .pattern-side { position: relative; width: 135px; height: 100%;
    background: linear-gradient(135deg, #d6d6d6, var(--pattern-mid) 45%, #cfcfcf); }
  .card-back .brand-box { left: 10px; top: 60px; width: 121px; height: 30px; }
  .card-back .pattern-side .tagline { left: 0; top: 96px; width: 100%; font-size: 8px; color: var(--ink);
    background: var(--paper); padding: 1px 0; }
  .card-back .info-side { width: 116px; height: 100%; background: var(--black-card); color: #d9d9d9;
    font-family: "Cormorant Garamond", serif; font-weight: 500; text-align: center; position: relative; }
  .info-side .person { position: absolute; top: 28px; width: 100%; font-family: "Great Vibes", cursive; font-size: 14px; color: var(--gold); }
  .info-side .role { position: absolute; top: 47px; width: 100%; font-family: "Great Vibes", cursive; font-size: 9px; color: var(--gold); }
  .info-side .contact { position: absolute; top: 82px; width: 100%; font-size: 8px; line-height: 12px; }
  .info-side .contact .email { font-size: 5.5px; }
</style>
</head>
<body>
<main class="canvas">

  <section class="sheet letterhead" aria-label="Letterhead">
    <div class="pattern" role="img" aria-label="Faint repeating monogram ornament pattern"></div>
    <div class="rule"></div>
    <span class="meta phone">555.555.555</span>
    <span class="meta note">dolo magnia qui aute</span>
    <div class="brand-box">
      <span class="brand-dot" style="width:16px;height:16px"></span>
      <span class="brand-name"><span class="word" style="font-size:19px">DOVE</span><span class="word" style="font-size:7px;letter-spacing:2px;margin-top:2px">INTERIORS</span></span>
    </div>
  </section>

  <section class="sheet envelope-back" aria-label="Envelope, address side">
    <div class="brand-box">
      <span class="brand-dot" style="width:10px;height:10px;border-width:1px"></span>
      <span class="brand-name"><span class="word" style="font-size:10px">DOVE</span><span class="word" style="font-size:4px;letter-spacing:1px;margin-top:1px">INTERIORS</span></span>
    </div>
    <div class="pattern" role="img" aria-label="Faint large monogram ornament"></div>
  </section>

  <section class="sheet envelope-front" aria-label="Envelope, flap side">
    <span class="brand-name"><span class="word" style="font-size:16px">DOVE</span><span class="word" style="font-size:6px;letter-spacing:2px;margin-top:2px">INTERIORS</span></span>
    <span class="tagline">Exquisite Furniture &amp; Furnishings</span>
  </section>

  <section class="sheet card-front" aria-label="Business card front">
    <span class="mark-ring"></span>
    <div class="band"></div>
    <span class="brand-name"><span class="word" style="font-size:19px;letter-spacing:2px">DOVE</span><span class="word" style="font-size:8px;letter-spacing:3px;margin-top:2px">INTERIORS</span></span>
    <span class="tagline">Exquisite Furniture &amp; Furnishings</span>
  </section>

  <section class="sheet card-back" aria-label="Business card back">
    <div class="pattern-side" role="img" aria-label="Black and grey monogram ornament pattern">
      <div class="brand-box">
        <span class="brand-dot" style="width:12px;height:12px"></span>
        <span class="brand-name"><span class="word" style="font-size:15px">DOVE</span><span class="word" style="font-size:5px;letter-spacing:2px;margin-top:1px">INTERIORS</span></span>
      </div>
      <span class="tagline">Exquisite Furniture &amp; Furnishings</span>
    </div>
    <div class="info-side">
      <p class="person">Helen Marchetti</p>
      <p class="role">Interior Stylist</p>
      <p class="contact">Mobile: 0432 871 264<br>PH: 03 9572 3140<br><span class="email">Email: helen@dove-interiors.com.au</span></p>
    </div>
  </section>

</main>
</body>
</html>
```